Corporate Design für Brandschutzplaner sucht cooperate Design
Zielgruppe
Wir sind Architekten und Brandschutzplaner - kleines Büro
(KWL - Kellmann-Wortberg-Lohse)
Unser Schwerpunkt liegt mit 80% bei allen Themen zum Brandschutz von Planung bis Begleitung der Umsetzung und zu 20% bei allen Bereich der Architektur.
Unsere Kunden sind gewerbliche Bauherren, öffentliche Bauherrn, Immobiliengesellschaften, private Bauherrn, ...
Aufgabenstellung
In der Anlage gibt es einige Beispiele unseres jetzigen Designs (noch ohne PartGmbB).
Das KWL würden wir gerne in dem Stiel erhalten, ebenfalls die blaue Farbe.
Grundsätzlich sind wir für Ideen offen. Auch bei der Richtung des Logos kann gerne abgewichen werden. Da wir selber kreativ sind, wissen wir, dass oft die gewinnen, die sich nicht an die Vorgaben halten :-)

```html
<!DOCTYPE html>
<html lang="de">
<head>
<meta charset="utf-8">
<title>KWL-Ingenieure – Geschäftsausstattung</title>
<link rel="stylesheet" href="https://fonts.googleapis.com/css2?family=Cabin:wght@400;600;700&display=swap">
<style>
  :root {
    --navy: #0d3a6c;
    --blue: #1f78b4;
    --red: #c8202b;
    --ink: #222;
    --paper: #ffffff;
    --stage: #e6e6e6;
    --hero: #f6f6f6;
  }
  * { box-sizing: border-box; margin: 0; padding: 0; }
  html, body { width: 1033px; height: 1200px; overflow: hidden; }
  body { background: var(--stage); font-family: "Cabin", sans-serif; color: var(--ink); position: relative; }

  .hero { position: absolute; left: 0; top: 0; width: 1033px; height: 235px; background: var(--hero); border-bottom: 1px solid #d4d4d4; }
  .hero-logo { position: absolute; left: 0; right: 0; top: 60px; text-align: center; }
  .hero-logo .brand-name { font-size: 62px; font-weight: 700; color: var(--navy); line-height: 1; letter-spacing: 1px; white-space: nowrap; }
  .hero-logo .brand-mark { display: inline-block; width: 16px; height: 16px; background: var(--red); margin-left: 8px; vertical-align: 6px; }
  .hero-logo .partners { font-size: 22px; font-weight: 700; color: var(--blue); margin-top: 10px; letter-spacing: .5px; }
  .hero-logo .tagline { font-size: 18px; color: var(--navy); margin-top: 4px; }

  .sheet { position: absolute; background: var(--paper); box-shadow: 3px 4px 8px rgba(0,0,0,.25); overflow: hidden; }

  /* logo lockup used on sheets and cards */
  .lockup { position: absolute; text-align: center; z-index: 2; }
  .lockup .brand-name { font-weight: 700; color: var(--navy); line-height: 1; white-space: nowrap; }
  .lockup .brand-mark { display: inline-block; background: var(--red); }
  .lockup .partners { display: inline-block; font-weight: 700; color: var(--blue); white-space: nowrap; background: var(--paper); }

  .rule-red { position: absolute; height: 2px; background: var(--red); z-index: 1; }
  .band-navy { position: absolute; background: var(--navy); color: #fff; white-space: nowrap; }

  /* letterhead */
  .letterhead { left: 28px; top: 280px; width: 471px; height: 664px; }
  .letterhead .lockup { right: 48px; top: 42px; width: 130px; }
  .letterhead .brand-name { font-size: 20px; }
  .letterhead .brand-mark { width: 6px; height: 6px; margin-left: 3px; vertical-align: 3px; }
  .letterhead .partners { font-size: 8.5px; line-height: 10px; margin-top: 3px; padding: 0 3px; }
  .letterhead .rule-top { left: 0; right: 0; top: 70px; }
  .letterhead .band-top { left: 0; right: 0; top: 76px; height: 11px; font-size: 6.8px; font-weight: 600; line-height: 11px; }
  .letterhead .band-top span { position: absolute; right: 48px; width: 130px; text-align: center; }
  .letter-body { position: absolute; left: 55px; top: 105px; width: 350px; font-size: 8.2px; line-height: 14.4px; }
  .sender-line { font-size: 5.6px; text-decoration: underline; line-height: 8px; }
  .recipient { margin-top: 14px; line-height: 11px; }
  .salutation { margin-top: 71px; }
  .body-text { margin-top: 17px; }
  .closing { margin-top: 16px; }
  .signature { width: 140px; height: 26px; margin: 2px 0 0 -4px; background: linear-gradient(90deg, rgba(40,40,40,.15), rgba(40,40,40,.05)); }
  .letterhead .rule-foot { left: 0; right: 0; top: 607px; }
  .letterhead .band-foot { left: 0; right: 0; top: 613px; height: 51px; display: flex; padding: 6px 0 0 33px; font-size: 5.8px; font-weight: 700; line-height: 8.8px; }
  .footer-col { width: 92px; }
  .footer-col.wide { width: 113px; }
  .footer-divider { width: 1px; background: #fff; margin: 0 12px 6px 0; }

  /* follow-up page */
  .follow-page { left: 527px; top: 280px; width: 472px; height: 664px; }
  .follow-page .lockup { right: 36px; top: 23px; width: 96px; }
  .follow-page .brand-name { font-size: 13px; }
  .follow-page .brand-mark { width: 4px; height: 4px; margin-left: 2px; vertical-align: 2px; }
  .follow-page .partners { font-size: 6px; line-height: 7px; margin-top: 2px; }
  .follow-page .tagline-small { font-size: 4.6px; color: var(--navy); white-space: nowrap; line-height: 6px; }
  .follow-page .edge-red { position: absolute; left: 454px; top: 0; bottom: 0; width: 2px; background: var(--red); }
  .follow-page .edge-navy { position: absolute; left: 461px; top: 0; bottom: 0; width: 11px; background: var(--navy); }

  /* business cards */
  .card { top: 972px; width: 306px; height: 199px; }
  .card-front { left: 178px; }
  .card-back { left: 530px; }
  .card .lockup { left: 78px; top: 43px; width: 150px; }
  .card .brand-name { font-size: 19px; }
  .card .brand-mark { width: 6px; height: 6px; margin-left: 3px; vertical-align: 3px; }
  .card .partners { font-size: 8.5px; line-height: 10px; margin-top: 3px; padding: 0 3px; }
  .card .rule-top { left: 0; right: 0; top: 73px; }
  .card .band-top { left: 0; right: 0; top: 79px; height: 10px; font-size: 7px; text-align: center; line-height: 10px; }
  .card-name { position: absolute; left: 50px; top: 108px; font-size: 9.5px; font-weight: 700; color: var(--navy); line-height: 12px; }
  .card-role { display: block; font-size: 6.5px; font-weight: 400; font-style: italic; color: var(--navy); margin-top: 1px; line-height: 8px; }
  .card-contact { position: absolute; left: 150px; top: 108px; font-size: 9px; line-height: 12px; color: var(--navy); white-space: nowrap; }
  .seal { position: absolute; left: 23px; top: 99px; }
  .card-web { position: absolute; left: 164px; top: 137px; font-size: 9.5px; font-weight: 700; color: var(--navy); white-space: nowrap; }
</style>
</head>
<body>

<header class="hero">
  <div class="hero-logo">
    <div class="brand-name">KWL-Ingenieure<span class="brand-mark"></span></div>
    <div class="partners">Brenner &amp; Pendrick PartGmbB</div>
    <div class="tagline">Kellmann · Wortberg · Lohse</div>
  </div>
</header>

<section class="sheet letterhead">
  <div class="lockup">
    <div class="brand-name">KWL-Ingenieure<span class="brand-mark"></span></div>
    <div class="partners">Brenner &amp; Pendrick PartGmbB</div>
  </div>
  <div class="rule-red rule-top"></div>
  <div class="band-navy band-top"><span>Kellmann · Wortberg · Lohse</span></div>

  <div class="letter-body">
    <p class="sender-line">Ihre Firma GmbH, Marktplatz 3, 10180 Berlin</p>
    <p class="recipient">Firma Norvalit GmbH<br>Paul Ebeling<br>Hafenstraße 5<br>10200 Berlin</p>
    <p class="salutation">Sehr geehrte Damen und Herren,</p>
    <p class="body-text">Lorem ipsum dolor sit amet, consetetur sadipscing elitr, sed diam nonumy eirmod tempor invidunt ut labore et dolore magna aliquyam erat, sed diam voluptua. At vero eos et accusam et justo duo dolores et ea rebum. Stet clita kasd gubergren, no sea takimata sanctus est Lorem ipsum dolor sit amet. Lorem ipsum dolor sit amet, consetetur sadipscing elitr, sed diam nonumy eirmod tempor invidunt ut labore et dolore magna aliquyam erat, sed diam voluptua. At vero eos et accusam et justo duo dolores et ea rebum. Stet clita kasd gubergren, no sea takimata sanctus est Lorem ipsum dolor sit amet.<br>Lorem ipsum dolor sit amet, consetetur sadipscing elitr, sed diam nonumy eirmod tempor invidunt ut labore et dolore magna aliquyam erat, sed diam voluptua. At vero eos et accusam et justo duo dolores et ea rebum. Stet clita kasd gubergren, no sea takimata sanctus est Lorem ipsum dolor sit amet. Lorem ipsum dolor sit amet, consetetur sadipscing elitr, sed diam nonumy eirmod tempor invidunt ut labore et dolore magna aliquyam erat, sed diam voluptua. At vero eos et accusam et justo duo dolores et ea rebum. Stet clita kasd gubergren, no sea takimata sanctus est Lorem ipsum dolor sit amet.</p>
    <p class="closing">Mit freundlichen Grüßen</p>
    <div class="signature" role="img" aria-label="Handschriftliche Unterschrift"></div>
    <p>Anton Reiser</p>
  </div>

  <div class="rule-red rule-foot"></div>
  <footer class="band-navy band-foot">
    <div class="footer-col">KWL-Ingenieure<br>Dipl.-Ing. (FH) Jonas Brenner<br>Erlenweg 9<br>23800 Nordstedt</div>
    <div class="footer-col wide">fon 04510 - 41 20 63<br>fax 04510 - 41 20 64<br>mobil 0152 - 71 08 44 29<br>mail brenner@kwl-ingenieure.de</div>
    <div class="footer-divider"></div>
    <div class="footer-col wide">KWL-Ingenieure<br>Dipl.-Ing. (FH) Lukas Pendrick<br>Birkenstraße 12<br>24650 Feldhusen</div>
    <div class="footer-col wide">fon 04190 - 38 15 22<br>fax 04190 - 38 15 23<br>mobil 0160 - 2 58 61 37<br>mail pendrick@kwl-ingenieure.de</div>
  </footer>
</section>

<section class="sheet follow-page">
  <div class="lockup">
    <div class="brand-name">KWL-Ingenieure<span class="brand-mark"></span></div>
    <div class="partners">Brenner &amp; Pendrick PartGmbB</div>
    <div class="tagline-small">Kellmann · Wortberg · Lohse</div>
  </div>
  <div class="edge-red"></div>
  <div class="edge-navy"></div>
</section>

<section class="sheet card card-front">
  <div class="lockup">
    <div class="brand-name">KWL-Ingenieure<span class="brand-mark"></span></div>
    <div class="partners">Brenner &amp; Pendrick PartGmbB</div>
  </div>
  <div class="rule-red rule-top"></div>
  <div class="band-navy band-top">Kellmann · Wortberg · Lohse</div>
  <div class="card-name">Jonas Brenner<span class="card-role">Dipl.-Ing. (FH) Architekt</span></div>
  <div class="card-contact">Erlenweg 9<br>23800 Nordstedt<br>fon: 04510 - 41 20 63<br>fax: 04510 - 41 20 64<br>mobil: 0152 - 71 08 44 29<br>mail: brenner@kwl-ingenieure.de</div>
</section>

<section class="sheet card card-back">
  <div class="lockup">
    <div class="brand-name">KWL-Ingenieure<span class="brand-mark"></span></div>
    <div class="partners">Brenner &amp; Pendrick PartGmbB</div>
  </div>
  <div class="rule-red rule-top"></div>
  <div class="band-navy band-top">Kellmann · Wortberg · Lohse</div>
  <svg class="seal" width="120" height="88" viewBox="0 0 120 88" role="img" aria-label="Siegel Sachverständiger">
    <ellipse cx="60" cy="44" rx="58" ry="42" fill="none" stroke="#555" stroke-width="1"/>
  </svg>
  <div class="card-web">www.kwl-ingenieure.de</div>
</section>

</body>
</html>
```